依頼詳細
プロが業務用の高圧洗浄機を使い、ご自宅の外構・駐車場(ガレージ)・ブロック塀・玄関タイル・を綺麗にされたい方を募集します。
泥、排気ガスの汚れ、コケ、ほこり等を綺麗に致します。
お見積りは無料
高圧洗浄専門店
割引制度有
平日割引あり(火曜日・水曜日は特別料金にて実施)(空き状況はお電話にてご確認下さい)
施工料金等、丁寧に分かりやすくご説明します。
作業時間平均:2時間~3時間
料金:33,000円~
作業時:水道をお借りします
まずは、お気軽にご相談下さい。
株式会社ミドリノハウジング
TEL:094ー318-5562
担当:坂巻(さかまき)・梅沢(うめざわ)
営業時間:9:00~19:00

記載項目
株式会社ミドリノハウジング
094-318-5562
料金:33,000円~(範囲によって異なります)
プロの高圧洗浄はミドリノハウジングにお任せください。
サイズ
A4
ページ数
片面
希望イメージ
シンプル 複雑
単色 カラフル
暗い 明るい
日常 高級
遊び心 厳粛
未来的 伝統的
女性的 男性的
希望する色
水色系、ターコイズブルーの使用をお願い致します。
納品ファイル
• 高解像度JPG (.jpg)
補足説明
会社ロゴを添付しておりますので、ロゴの使用をお願い致します。
■ 選んだ理由

見やすく、弊社希望のチラシに近いものでした。
頂きました案件全てのチラシ案を印刷し、三つ折りにしましたが、一番良かったです。
伝えたい内容も、しっかり入っており、戸建てとなると年配の方が多いと思われ、その点でも大事な部分は文字が大きく見やすさも良く選ばせて頂きました。

■ 提案者全員のお礼・コメント

初めての依頼となりましたが、多数の応募を頂きましてありがとうございました。
正直、こんなに多数の応募を頂けるとは思ってませんでしたので驚きました。
今後もチラシの案をご依頼する事もるかと思いますので、宜しくお願い致します。

```html
<!DOCTYPE html>
<html lang="ja">
<head>
<meta charset="utf-8">
<title>お家まわりの高圧洗浄 | 株式会社ミドリノハウジング</title>
<link href="https://fonts.googleapis.com/css2?family=M+PLUS+Rounded+1c:wght@500;700;800;900&display=swap" rel="stylesheet">
<style>
:root{
  --sky:#8fd8ea;
  --sky-deep:#5cc2dc;
  --navy:#1d4f8f;
  --blue:#1f7fc4;
  --yellow:#ffe632;
  --red:#e5302a;
  --white:#ffffff;
  --ink:#2a2a2a;
}
*{margin:0;padding:0;box-sizing:border-box}
html,body{width:849px;height:1200px;overflow:hidden;background:#fff}
body{font-family:"M PLUS Rounded 1c",sans-serif;color:var(--ink)}
.flyer{position:relative;width:849px;height:1200px;background:var(--sky);overflow:hidden}
.splash{position:absolute;left:-80px;top:60px;width:440px;height:520px;border-radius:50%;background:var(--sky-deep);opacity:.3}
.tagline{position:absolute;top:14px;left:0;right:0;text-align:center;color:var(--white);font-weight:700;font-size:23px;letter-spacing:1px;line-height:1.2}
.plan-banner{position:absolute;left:212px;top:56px;width:425px;height:48px;background:var(--yellow);border-radius:8px;display:flex;align-items:center;justify-content:center;color:var(--red);font-weight:900;font-size:34px;letter-spacing:1px;line-height:1}
.headline{position:absolute;top:106px;left:0;right:0;text-align:center;color:var(--white);font-weight:900;font-size:56px;line-height:1.2;letter-spacing:1px;text-shadow:0 3px 0 var(--navy)}
.price{position:absolute;top:168px;left:150px;color:var(--yellow);font-weight:900;font-size:96px;line-height:1;letter-spacing:1px;text-shadow:0 4px 0 var(--navy)}
.price small{font-size:44px}
.mascot-top{position:absolute;left:665px;top:185px;width:165px;height:175px;border-radius:40% 40% 20% 20%;background:linear-gradient(#e9b98a,#c98a55)}
.badges{position:absolute;left:147px;top:275px;display:flex;gap:22px}
.badge{width:115px;height:88px;background:var(--white);border-radius:12px;display:flex;align-items:center;justify-content:center;text-align:center;color:var(--blue);font-weight:900;font-size:26px;line-height:1.2}
.note{position:absolute;top:376px;left:0;right:0;text-align:center;color:var(--white);font-size:14px;font-weight:700;line-height:1.2}
.panel{position:absolute;left:22px;top:408px;width:805px;height:778px;background:var(--white);border-radius:20px}
.intro{position:absolute;left:48px;top:424px;width:756px;font-size:22px;font-weight:700;line-height:1.6;color:var(--ink)}
.intro .hl{color:var(--blue)}
.photo{position:absolute;left:95px;width:205px;height:118px;border-radius:4px}
.photo-a{top:592px;background:linear-gradient(135deg,#8a8f88,#c3c7bf)}
.photo-b{top:716px;background:linear-gradient(135deg,#b98a80,#e6d2c6)}
.facts{position:absolute;left:328px;top:604px;list-style:none;font-size:21px;font-weight:700;line-height:1.6}
.facts li::before{content:"■";color:var(--blue);margin-right:4px}
.facts small{font-size:13px}
.mascot-low{position:absolute;left:28px;top:842px;width:115px;height:122px;border-radius:40%;background:linear-gradient(#e9b98a,#c98a55)}
.cta{position:absolute;top:968px;left:150px;color:var(--blue);font-weight:900;font-size:34px;line-height:1.2}
.phone{position:absolute;left:150px;top:1022px;display:flex;align-items:center;gap:10px;color:var(--navy);font-weight:900;font-size:56px;line-height:1}
.phone svg{width:54px;height:48px}
.brand{position:absolute;left:665px;top:1000px;width:150px;text-align:center}
.brand .mark{width:60px;height:60px;background:var(--sky-deep);display:inline-block;margin-bottom:8px}
.brand span{display:block;font-size:16px;font-weight:800;color:var(--navy);white-space:nowrap}
.company{position:absolute;left:150px;top:1094px;font-size:24px;font-weight:800;color:var(--navy);line-height:1.2}
.footer{position:absolute;left:60px;top:1142px;font-size:19px;font-weight:700;color:var(--ink);line-height:1.2}
.footer .sep{margin:0 16px}
</style>
</head>
<body>
<div class="flyer">
  <div class="splash"></div>
  <p class="tagline">プロの高圧洗浄はミドリノハウジングにお任せください</p>
  <div class="plan-banner">平日格安プラン実施中!!</div>
  <h1 class="headline">お家まわりの高圧洗浄</h1>
  <p class="price">33,000<small>円~</small></p>
  <div class="mascot-top" role="img" aria-label="高圧洗浄機を持った作業着姿のたぬきのキャラクター"></div>
  <div class="badges">
    <div class="badge">割引<br>制度有</div>
    <div class="badge">平日<br>割引</div>
    <div class="badge">お見積<br>無料</div>
  </div>
  <p class="note">※火曜日・水曜日は特別料金にて実施、空き状況はお電話にてご確認下さい。</p>

  <div class="panel"></div>
  <p class="intro">プロが<span class="hl">業務用の高圧洗浄機</span>を使い、ご自宅の外構・駐車場(ガレージ)・ブロック塀・玄関タイルなどに付着した泥、排気ガスの汚れ、コケ、ほこり等を綺麗に致します。「何年も放置している」という方や「一度も洗浄したことがない」という方も大歓迎です!!</p>
  <div class="photo photo-a" role="img" aria-label="高圧洗浄中のブロック塀の写真"></div>
  <div class="photo photo-b" role="img" aria-label="洗浄後の玄関タイルの写真"></div>
  <ul class="facts">
    <li>作業時間平均:2時間~3時間</li>
    <li>料金:33,000円~<small>(範囲によって異なります)</small></li>
    <li>作業時:水道をお借りします</li>
    <li>お見積もり無料:施工料金等、<br>　丁寧に分かりやすくご説明します。</li>
  </ul>

  <div class="mascot-low" role="img" aria-label="手を振るたぬきのキャラクター"></div>
  <p class="cta">まずはお気軽にご相談ください!</p>
  <div class="phone">
    <svg viewBox="0 0 64 56" aria-hidden="true"><path d="M8 18c0-8 10-12 24-12s24 4 24 12v4H44v-6H20v6H8z" fill="#1d4f8f"/><rect x="12" y="26" width="40" height="26" rx="6" fill="#1d4f8f"/><circle cx="32" cy="39" r="7" fill="#fff"/></svg>
    <span>094-318-5562</span>
  </div>
  <div class="brand"><i class="mark"></i><span>ミドリノハウジング</span></div>
  <p class="company">株式会社ミドリノハウジング</p>
  <p class="footer">■担当/坂巻(さかまき)・梅沢(うめざわ)<span class="sep"></span>■営業時間/9:00~19:00</p>
</div>
</body>
</html>
```